Medical Eye Care Practice needs a unique business card design.

I need a business card for my medical, eye care practice. I am seeking a unique design, possibly with a vertical or atypical shape layout -- something to make the card stand out. I would like the final design to communicate health and wellness with a contemporary feel. Please incorporate my logo and slogan with a color scheme based off of my logo. It should also identify all of the information that is listed on my sample business card. The back side should be utilized for appointment reminder with date, time, and room for notes. I would also like some incorporation of facebook, twitter, and google plus links.

```html
<!DOCTYPE html>
<html lang="en">
<head>
<meta charset="utf-8">
<title>Appointment Card – Lakeshore Eye</title>
<link href="https://fonts.googleapis.com/css2?family=Arimo:wght@400;700&display=swap" rel="stylesheet">
<style>
  :root {
    --paper: #ffffff;
    --ink: #000000;
    --brand-stone: #8a8478;
    --brand-leaf: #9bb47a;
  }
  html, body {
    margin: 0;
    padding: 0;
    overflow: hidden;
    background: var(--paper);
  }
  .card {
    position: relative;
    width: 1200px;
    height: 686px;
    overflow: hidden;
    background: var(--paper);
    font-family: "Arimo", Arial, sans-serif;
    color: var(--ink);
  }
  .card__title {
    position: absolute;
    left: 0;
    right: 0;
    top: 52px;
    margin: 0;
    text-align: center;
    font-size: 56px;
    font-weight: 700;
    line-height: 1;
  }
  .field {
    position: absolute;
    margin: 0;
    font-size: 48px;
    font-weight: 400;
    line-height: 1;
  }
  .field--date { left: 109px; top: 150px; }
  .field--time { left: 737px; top: 150px; }
  .field--reason { left: 109px; top: 264px; }
  .brand {
    position: absolute;
    left: 64px;
    top: 518px;
    display: flex;
    align-items: center;
    gap: 12px;
  }
  .brand__dot {
    width: 30px;
    height: 30px;
    border-radius: 50%;
    background: var(--brand-leaf);
  }
  .brand__name {
    font-size: 30px;
    font-weight: 700;
    color: var(--brand-stone);
    line-height: 1;
  }
  .contact {
    position: absolute;
    left: 640px;
    width: 490px;
    top: 546px;
    text-align: center;
    font-size: 35px;
    font-weight: 700;
    line-height: 46px;
  }
  .contact p { margin: 0; }
</style>
</head>
<body>
  <div class="card">
    <h1 class="card__title">Appointment</h1>
    <p class="field field--date">Date:</p>
    <p class="field field--time">Time:</p>
    <p class="field field--reason">Reason for Visit:</p>

    <div class="brand">
      <span class="brand__dot"></span>
      <span class="brand__name">Lakeshore Eye</span>
    </div>

    <div class="contact">
      <p class="contact__web">www.lakeshore-eye.com</p>
      <p class="contact__phone">(555) 014-2873</p>
    </div>
  </div>
</body>
</html>
```